Thornfield Marsh, LLC Website

We are a small law firm in need of a website that contains the following:
1. Attractive main page
2. About us/attorney info for three people: Leonard Thornfield (attorney), Brent Marsh (attorney), and Melinda Carrow (legal assistant). We have bio's ready to submit.
3. Blog/video page. We'd like to post blogs and videos to help drive traffic
4. Multidistrict Litigation and Class Actions page, where we post information regarding active MDLs and Class actions that we are doing intake on.
Updates

Can you also please use the color "gold" in the design and logo? Thanks.

Industry/Entity Type

Legal

Coding

Coded - Design and coding required

Number of Pages Required

1 page

Colors
0054AA
0677BA
7BADD7
CADEEF
E8F1F8

Requirements
Must have
• 1. Attractive main page 2. About us/attorney info for three people: Leonard Thornfield (attorney), Brent Marsh (attorney), and Melinda Carrow (legal assistant). We have bio's ready to submit. 3. Blog/video page. We'd like to post blogs and videos to help drive traffic 4. Multidistrict Litigation and Class Actions page, where we post information regarding active MDLs and Class actions that we are doing intake on.

```html
<!DOCTYPE html>
<html lang="en">
<head>
<meta charset="utf-8">
<title>Thornfield Marsh, LLC — Lawyers</title>
<link href="https://fonts.googleapis.com/css2?family=Poppins:wght@400;500;600;700;800&display=swap" rel="stylesheet">
<style>
:root{
  --navy:#0b1c8c;
  --navy-deep:#0a1a7a;
  --sky:#1fa3f0;
  --gold:#d4a72c;
  --ink:#1b1b2b;
  --muted:#5b5f6b;
  --white:#ffffff;
  --line:#d9dce3;
}
*{box-sizing:border-box;margin:0;padding:0}
html,body{width:1200px;height:3764px;overflow:hidden}
body{position:relative;font-family:'Poppins',sans-serif;color:var(--ink);background:var(--white)}
.abs{position:absolute}
.photo{position:absolute}

/* header */
.brand{left:99px;top:29px;width:360px;height:63px;border:3px solid var(--navy);display:flex;align-items:center;background:var(--white)}
.brand-square{width:88px;height:100%;background:var(--gold)}
.brand-name{font-weight:600;font-size:22px;color:var(--sky);padding-left:16px;white-space:nowrap;line-height:1}
.nav{left:485px;top:29px;width:626px;height:65px;background:var(--white);box-shadow:0 2px 14px rgba(0,0,0,.08);display:flex;align-items:center;justify-content:space-around;padding:0 20px}
.nav a,.foot-nav a{font-weight:700;font-size:14px;color:var(--navy);text-decoration:none;letter-spacing:.2px}
.nav a.active{color:var(--sky)}

/* hero */
.hero{left:0;top:124px;width:1200px;height:506px;background:linear-gradient(90deg,#0a2f6e 0%,#0d4fa0 35%,#0a3c9a 60%,#0b2f95 100%)}
.hero-photo{left:0;top:0;width:620px;height:506px;background:radial-gradient(circle at 50% 45%,#2a8fd6 0%,#15529a 40%,transparent 75%)}
.hero h1{left:630px;top:152px;font-size:38px;line-height:44px;font-weight:700;color:var(--white)}
.hero p{left:631px;top:250px;width:420px;font-size:15.5px;line-height:21px;color:#e6eeff}
.btn{display:flex;height:46px;text-decoration:none}
.btn-icon{width:46px;background:var(--navy);display:flex;align-items:center;justify-content:center}
.btn-label{background:var(--sky);color:var(--white);font-weight:700;font-size:14px;display:flex;align-items:center;padding:0 15px}

/* welcome */
.welcome-frame{left:105px;top:742px;width:240px;height:94px;border-left:3px solid var(--sky);border-top:3px solid var(--sky);border-bottom:3px solid var(--sky)}
.welcome-title{left:127px;top:748px;font-size:35px;line-height:39px;font-weight:700;color:var(--navy);white-space:nowrap}
.welcome-title span{color:var(--sky)}
.welcome-text{left:127px;top:857px;width:445px;font-size:16px;line-height:24px;color:var(--muted)}
.meeting-photo{left:617px;top:732px;width:454px;height:285px;background:linear-gradient(135deg,#8fa6b8,#4b5d70 55%,#c9c2b4)}
.justice-photo{left:813px;top:949px;width:222px;height:185px;background:linear-gradient(135deg,#efe6e0,#b98a6a 55%,#5c3a2c);border:6px solid var(--white);box-sizing:content-box}

/* team */
.team{left:0;top:1201px;width:1200px;height:641px;background:linear-gradient(90deg,#2eb0f2,#1c9ae0)}
.team-title-frame{left:599px;top:69px;width:152px;height:70px;border-top:3px solid var(--white);border-right:3px solid var(--white);border-bottom:3px solid var(--white)}
.team-title{left:0;width:1200px;top:83px;text-align:center;font-size:34px;font-weight:700;color:var(--white)}
.member{width:236px;text-align:center}
.member-frame{width:236px;height:238px;border:3px solid var(--white);padding:12px}
.member-photo{width:100%;height:100%;background:linear-gradient(160deg,#a9b4bf,#3c4a5c)}
.member-name{margin-top:26px;font-weight:700;font-size:17px;color:var(--white);white-space:nowrap}
.member-role{font-size:17px;color:var(--white);margin-top:4px}

/* blog */
.blog-title{left:0;width:1200px;top:1958px;text-align:center;font-size:33px;font-weight:700;color:var(--navy)}
.blog-title span{color:var(--sky)}
.post-main{left:127px;top:2037px;width:532px;height:484px;border:1px solid var(--line)}
.post-main-photo{left:0;top:0;width:530px;height:305px;background:linear-gradient(135deg,#c9c3bc,#6b6f78 50%,#e2ddd6)}
.post-main h3{left:40px;top:330px;width:450px;font-size:23px;line-height:30px;font-weight:700;color:var(--sky)}
.post-main p{left:40px;top:412px;width:450px;font-size:15px;line-height:21px;color:var(--muted)}
.post{left:688px;width:420px;height:147px}
.post-photo{left:0;top:0;width:160px;height:147px}
.post h4{left:185px;top:10px;width:215px;font-size:16.5px;line-height:21px;font-weight:700;color:var(--navy)}
.post p{left:185px;top:62px;width:215px;font-size:12.5px;line-height:17px;color:#8a8d96}
.post time{left:185px;top:110px;font-size:14px;font-weight:700;color:var(--sky)}

/* litigation */
.mdl{left:0;top:2650px;width:1200px;height:618px;background:linear-gradient(90deg,#c9ccd2,#e9eaec 50%,#f2f2f3)}
.mdl-photo{left:0;top:0;width:560px;height:618px;background:linear-gradient(120deg,#d3cfca,#6f6760 45%,#1c2433 75%,#dcdcdc)}
.mdl h2{left:596px;top:175px;font-size:34px;line-height:38px;font-weight:700;color:var(--navy)}
.mdl p{left:594px;top:285px;width:470px;font-size:15.5px;line-height:21px;color:var(--ink)}

/* footer */
.footer{left:0;top:3313px;width:1200px;height:451px;background:linear-gradient(135deg,#0c1f93,#0a1a80 60%,#0d2296)}
.foot-nav{left:0;top:98px;width:1200px;display:flex;justify-content:center;gap:58px}
.foot-nav a{color:var(--white)}
.contact{top:170px;display:flex;align-items:center;gap:16px}
.contact-icon{width:60px;height:56px;background:var(--sky);display:flex;align-items:center;justify-content:center;flex:none}
.contact-text{font-size:17.5px;line-height:22px;color:var(--white);white-space:nowrap}
.foot-bar{left:127px;top:302px;width:944px;height:67px;background:var(--white)}
.foot-brand{left:10px;top:10px;width:244px;height:46px;border:3px solid var(--navy);display:flex;align-items:center}
.foot-brand .brand-square{width:48px}
.foot-brand .brand-name{font-size:17px;padding-left:10px}
.copyright{left:0;width:944px;top:23px;text-align:center;font-size:15px;color:var(--ink)}
.social{top:13px;width:40px;height:40px;border-radius:50%;background:var(--sky)}
</style>
</head>
<body>

<header>
  <div class="abs brand"><div class="brand-square"></div><div class="brand-name">THORNFIELD MARSH LLC</div></div>
  <nav class="abs nav">
    <a class="active" href="#">HOME</a><a href="#">ABOUT US</a><a href="#">BLOG</a><a href="#">MULTIDISTRICT LITIGATION</a>
  </nav>
</header>

<section class="abs hero">
  <div class="photo hero-photo" role="img" aria-label="Hand of a man in a suit touching a glowing digital scales-of-justice interface"></div>
  <h1 class="abs">BUILD YOUR FUTURE<br>IN THE LAW INDUSTRY</h1>
  <p class="abs">Lorem ipsum dolor sit amet, consectetur adipiscing eli sed do eiusmod tempor incididunt ut labore et dolore magna aliqua uis ipsum suspendisse ultrice.</p>
  <a class="abs btn" href="#" style="left:630px;top:331px">
    <span class="btn-icon"><svg width="14" height="12" viewBox="0 0 14 12"><path d="M1 1l5 5-5 5M7 1l5 5-5 5" fill="none" stroke="#fff" stroke-width="2"/></svg></span>
    <span class="btn-label">GET STARTED</span>
  </a>
</section>

<section>
  <div class="abs welcome-frame"></div>
  <h2 class="abs welcome-title">WELCOME TO<br><span>THORNFIELD MARSH</span>, LLC</h2>
  <p class="abs welcome-text">Lorem ipsum dolor sit amet, consectetur adipiscing elit, sed do eiusmod tempor incididunt ut labore et dolore magna aliqua. Quis ipsum suspendisse ultrices gravid asus commodo vive rra Lorem ipsum dolor sit amet, consectetur adipiscing elit, sed do eiusmod tempor inc ididunt ut labore et dolore magna aliqua. Quis ipsum suspendisse ultrices gravida. Risus commodo vive rra maecenas accumsan lacus vel facilisis. maecenas accumsan lacus vel facilisis.</p>
  <div class="photo meeting-photo" role="img" aria-label="Lawyers meeting around a conference table"></div>
  <div class="photo justice-photo" role="img" aria-label="Statue of Lady Justice beside a gavel"></div>
</section>

<section class="abs team">
  <div class="abs team-title-frame"></div>
  <h2 class="abs team-title">ABOUT US</h2>
  <div class="abs member" style="left:165px;top:217px">
    <div class="member-frame"><div class="member-photo" role="img" aria-label="Portrait of attorney Leonard Thornfield"></div></div>
    <div class="member-name">LEONARD THORNFIELD</div><div class="member-role">Attorney</div>
  </div>
  <div class="abs member" style="left:482px;top:217px">
    <div class="member-frame"><div class="member-photo" role="img" aria-label="Portrait of attorney Brent Marsh"></div></div>
    <div class="member-name">BRENT MARSH</div><div class="member-role">Attorney</div>
  </div>
  <div class="abs member" style="left:795px;top:217px">
    <div class="member-frame"><div class="member-photo" role="img" aria-label="Portrait of legal assistant Melinda Carrow"></div></div>
    <div class="member-name">MELINDA CARROW</div><div class="member-role">Legal Assistant</div>
  </div>
</section>

<section>
  <h2 class="abs blog-title">LATEST <span>BLOG POSTS</span></h2>
  <article class="abs post-main">
    <div class="photo post-main-photo" role="img" aria-label="Team of lawyers in discussion at a table"></div>
    <h3 class="abs">Lorem ipsum dolor sit amet, consect etur adipiscing elit ed do eiusmod.</h3>
    <p class="abs">Lorem ipsum dolor sit amet, consectetur adipiscing elit, sed do eiusmod tempor incididunt ut labore.</p>
  </article>
  <article class="abs post" style="top:2037px">
    <div class="photo post-photo" role="img" aria-label="Law books with a gavel" style="background:linear-gradient(135deg,#d8c8b0,#6c5a48)"></div>
    <h4 class="abs">Lorem ipsum dolor sit amet, consectetur.</h4>
    <p class="abs">Lorem ipsum dolor sit amet, consectetur adipiscing.</p>
    <time class="abs">Apr 05 2025</time>
  </article>
  <article class="abs post" style="top:2205px">
    <div class="photo post-photo" role="img" aria-label="Hands signing a document" style="background:linear-gradient(135deg,#e4e6f0,#c9a2b4)"></div>
    <h4 class="abs">Lorem ipsum dolor sit amet, consectetur.</h4>
    <p class="abs">Lorem ipsum dolor sit amet, consectetur adipiscing.</p>
    <time class="abs">Apr 05 2025</time>
  </article>
  <article class="abs post" style="top:2375px">
    <div class="photo post-photo" role="img" aria-label="Woman working at a laptop" style="background:linear-gradient(135deg,#cfd2cc,#54524c)"></div>
    <h4 class="abs">Lorem ipsum dolor sit amet, consectetur.</h4>
    <p class="abs">Lorem ipsum dolor sit amet, consectetur adipiscing.</p>
    <time class="abs">Apr 05 2025</time>
  </article>
</section>

<section class="abs mdl">
  <div class="photo mdl-photo" role="img" aria-label="Young graduate in a gown reading a folder"></div>
  <h2 class="abs">MULTIDISTRICT LITIGATION<br>AND CLASS ACTIONS</h2>
  <p class="abs">Lorem ipsum dolor sit amet, consectetur adipiscing elit, sed do eiusmod tempor incididunt ut labore et dolore magna aliqua. Quis ipsum suspendisse ultrices gravida. Risus comm odo viverra maecenas accumsan lacus vel facilisis.</p>
  <a class="abs btn" href="#" style="left:597px;top:392px">
    <span class="btn-icon"><svg width="14" height="12" viewBox="0 0 14 12"><path d="M1 1l5 5-5 5M7 1l5 5-5 5" fill="none" stroke="#fff" stroke-width="2"/></svg></span>
    <span class="btn-label">READ MORE</span>
  </a>
</section>

<footer class="abs footer">
  <nav class="abs foot-nav"><a href="#">HOME</a><a href="#">ABOUT US</a><a href="#">BLOG</a><a href="#">MULTIDISTRICT LITIGATION</a></nav>
  <div class="abs contact" style="left:199px">
    <span class="contact-icon"><svg width="22" height="16" viewBox="0 0 22 16"><rect x="1" y="1" width="20" height="14" fill="#fff"/><path d="M1 1l10 8 10-8" fill="none" stroke="#1fa3f0" stroke-width="2"/></svg></span>
    <span class="contact-text">Email:<br>info@tmfirm.com</span>
  </div>
  <div class="abs contact" style="left:504px">
    <span class="contact-icon"><svg width="20" height="20" viewBox="0 0 20 20"><rect x="1" y="1" width="18" height="18" rx="3" fill="#fff"/><path d="M6 5c0 5 4 9 9 9l1-2-3-2-1 1c-2-1-3-2-4-4l1-1-2-3z" fill="#1fa3f0"/></svg></span>
    <span class="contact-text">Phone:<br>555 0142 7731</span>
  </div>
  <div class="abs contact" style="left:753px">
    <span class="contact-icon"><svg width="16" height="22" viewBox="0 0 16 22"><path d="M8 1a7 7 0 0 0-7 7c0 5 7 13 7 13s7-8 7-13a7 7 0 0 0-7-7z" fill="#fff"/><circle cx="8" cy="8" r="3" fill="#1fa3f0"/></svg></span>
    <span class="contact-text">Location:<br>Lorem usm 364 Lore</span>
  </div>
  <div class="abs foot-bar">
    <div class="abs foot-brand"><div class="brand-square"></div><div class="brand-name">THORNFIELD MARSH</div></div>
    <p class="abs copyright">Copyright © 2025 All Rights Are Reserved.</p>
    <span class="abs social" style="left:787px"></span>
    <span class="abs social" style="left:833px"></span>
    <span class="abs social" style="left:878px"></span>
  </div>
</footer>

</body>
</html>
```